Bright Oak Fitness Facility Business Cards

Business Card Design that incorporates the logo and tagline

Target Market(s)

Fitness, People Who Exercise

Contact Information for Business Card

2817 Mossgrove Bend Road
Millbrook Hollow, Vermont 05190
Phone: 555-019-Jump (5867)
www.brightoakfitness.example
info@brightoakfitness.example

Requirements
Must have
• Logo, Address, Website, email and tagline "More Than A Gym". Colors should be red/black/grey/white

```html
<!DOCTYPE html>
<html lang="en">
<head>
<meta charset="utf-8">
<title>Bright Oak Fitness Facility – Business Card</title>
<link href="https://fonts.googleapis.com/css2?family=Montserrat:wght@700;800&family=Roboto:wght@400;500&display=swap" rel="stylesheet">
<style>
  :root {
    --brand-red: #e3212b;
    --ink: #161616;
    --paper: #ffffff;
    --stage: #e6e6e6;
    --mark-peach: #f1cfc1;
    --mark-grey: #c9c9c9;
  }
  * { box-sizing: border-box; margin: 0; padding: 0; }
  html, body {
    width: 1200px; height: 871px; overflow: hidden;
    background: var(--stage);
  }
  .card {
    position: absolute; left: 75px; top: 135px;
    width: 1050px; height: 600px;
    background: var(--paper);
    box-shadow: 0 10px 30px rgba(0,0,0,.18);
    overflow: hidden;
  }
  .brand {
    position: absolute; left: 90px; top: 92px;
    display: flex; align-items: center; gap: 14px;
  }
  .brand-square {
    width: 30px; height: 30px; background: var(--brand-red); flex: none;
  }
  .brand-name {
    font-family: "Montserrat", sans-serif; font-weight: 800;
    font-size: 36px; line-height: 1.05; letter-spacing: .5px;
    color: var(--brand-red); text-transform: uppercase;
  }
  .brand-rule {
    position: absolute; left: 90px; top: 200px;
    width: 330px; height: 3px; background: var(--ink);
  }
  .contact {
    position: absolute; left: 90px; top: 240px;
    font-family: "Roboto", sans-serif; font-size: 22px;
    line-height: 1.45; color: var(--ink);
  }
  .address { margin-bottom: 10px; }
  .contact-row { display: flex; align-items: center; gap: 12px; }
  .contact-row svg { width: 22px; height: 22px; flex: none; }
  .tagline {
    position: absolute; right: 100px; top: 215px;
    font-family: "Montserrat", sans-serif; font-weight: 700;
    font-size: 34px; letter-spacing: 1px; color: var(--ink);
    text-transform: uppercase; white-space: nowrap;
  }
  .faint-mark {
    position: absolute; left: 560px; top: 330px;
    width: 490px; height: 270px;
    background: linear-gradient(160deg, var(--mark-peach) 0%, #f7e4dc 55%, var(--mark-grey) 100%);
    opacity: .55;
    border-top-left-radius: 260px 270px;
    z-index: 1;
  }
  .edge-tab {
    position: absolute; right: 0; top: 285px;
    width: 22px; height: 52px; background: var(--brand-red);
    z-index: 2;
  }
</style>
</head>
<body>
  <main class="card">
    <div class="brand">
      <span class="brand-square"></span>
      <span class="brand-name">Bright Oak<br>Fitness</span>
    </div>
    <div class="brand-rule"></div>

    <section class="contact">
      <p class="address">2817 Mossgrove Bend Road<br>Millbrook Hollow, Vermont 05190</p>
      <p class="contact-row">
        <svg viewBox="0 0 24 24" aria-hidden="true"><circle cx="12" cy="12" r="12" fill="#e3212b"/><path d="M8.5 6.5l2 2.3-1.2 1.4c.8 1.7 2 2.9 3.6 3.7l1.4-1.2 2.3 2-1.3 1.8c-4.3-.6-7.9-4.2-8.4-8.5z" fill="#fff"/></svg>
        555-019-Jump (5867)
      </p>
      <p class="contact-row">
        <svg viewBox="0 0 24 24" aria-hidden="true"><circle cx="12" cy="12" r="12" fill="#e3212b"/><rect x="6" y="8" width="12" height="8.5" rx="1" fill="#fff"/><path d="M6.3 8.4l5.7 4.3 5.7-4.3" stroke="#e3212b" stroke-width="1.3" fill="none"/></svg>
        info@brightoakfitness.example
      </p>
      <p class="contact-row">
        <svg viewBox="0 0 24 24" aria-hidden="true"><circle cx="12" cy="12" r="12" fill="#e3212b"/><circle cx="12" cy="12" r="6" fill="none" stroke="#fff" stroke-width="1.4"/><ellipse cx="12" cy="12" rx="2.6" ry="6" fill="none" stroke="#fff" stroke-width="1.2"/><path d="M6 12h12" stroke="#fff" stroke-width="1.2"/></svg>
        www.brightoakfitness.example
      </p>
    </section>

    <h2 class="tagline">More Than A Gym</h2>
    <div class="faint-mark" role="img" aria-label="Faint oversized brand emblem decoration"></div>
    <div class="edge-tab"></div>
  </main>
</body>
</html>
```